Clockharbour Homepage Banner 1060 W x 100 H

Please see the attached 'word' document (Also copied below)
Feel free to use any images or logos from our website.
www.clockharbour.com.au

Background:
We are an Australian based official watch distributor/online retailer of international watch brands.

We require a new banner ad (1060 W x 100 H) to replace the existing one on our homepage www.clockharbour.com.au & wish to convey the following information:
*(Please feel free to alter wording, include or exclude points below & generally take creative license (with commercial reality in mind). We sell some luxury watches, so it must look professional & maintain a luxury look & feel.)

Clockharbour Direct:
Revolutionising the retail watch market !

- Buy direct from the official distributor & get world competitive
online prices (with full international warranty, & all original
papers, box & invoice)

- Eliminate all risk of fakes & non-existent factory warranty from
'grey' market sellers

- Free worldwide delivery over A$300

- Order online & 'try-on' in the comfort of your own home.
If you're not 100% happy, just post it back for a full refund or
exchange within 30 days

- Prefer to see & try on before purchase? Visit one of our retail
partner stores.

*** Feel free to copy any images from our website
www.clockharbour.com.au
Updates

Target Market(s)

Luxury watches

Industry/Entity Type

Retail

Font styles to use
Sans Serif

Requirements
Must have
• Visual imagery, text
Nice to have
• Feel free to use your creativity...
Should not have
• Cheap looking or tacky images. We sell some luxury watches, so we need to keep a professional & luxury image.

```html
<!DOCTYPE html>
<html lang="en">
<head>
<meta charset="utf-8">
<title>Clockharbour Homepage Banner</title>
<link rel="stylesheet" href="https://fonts.googleapis.com/css2?family=Open+Sans:wght@300;400;600;700&display=swap">
<style>
  :root {
    --page-bg: #e9e6e2;
    --banner-black: #000000;
    --accent-blue: #5aa9e0;
    --text-white: #ffffff;
    --logo-navy: #1d3b6e;
    --photo-dark: #1c2a44;
    --photo-steel: #9aa3ad;
  }
  * { margin: 0; padding: 0; box-sizing: border-box; }
  html, body {
    width: 1200px;
    height: 408px;
    overflow: hidden;
    background: var(--page-bg);
    font-family: "Open Sans", Arial, sans-serif;
  }
  .banner {
    position: absolute;
    left: 17px;
    top: 149px;
    width: 1166px;
    height: 110px;
    background: var(--banner-black);
    overflow: hidden;
    color: var(--text-white);
  }
  .banner__photo {
    position: absolute;
    left: 0;
    top: 0;
    width: 184px;
    height: 110px;
    background: radial-gradient(circle at 50% 50%, var(--photo-dark) 0 36%, var(--photo-steel) 38% 46%, #2b2f36 60%, var(--banner-black) 78%);
  }
  .banner__question {
    position: absolute;
    left: 198px;
    top: 42px;
    font-size: 20.5px;
    font-weight: 600;
    white-space: nowrap;
    letter-spacing: 0.1px;
  }
  .offer {
    position: absolute;
    left: 643px;
    top: 7px;
    line-height: 1;
  }
  .offer__lead {
    display: block;
    font-size: 34px;
    font-weight: 300;
  }
  .offer__amount {
    display: block;
    margin-top: 5px;
    font-size: 44px;
    font-weight: 700;
    letter-spacing: 0.3px;
  }
  .banner__arcs {
    position: absolute;
    left: 0;
    top: 0;
  }
  .brand {
    position: absolute;
    left: 961px;
    top: 13px;
    display: flex;
    align-items: center;
    gap: 8px;
  }
  .brand__dot {
    width: 24px;
    height: 24px;
    border-radius: 50%;
    background: var(--logo-navy);
  }
  .brand__name {
    font-size: 20px;
    font-weight: 600;
    color: var(--logo-navy);
  }
  .cta {
    position: absolute;
    left: 953px;
    top: 54px;
    width: 198px;
    height: 40px;
    border: 1.5px solid var(--text-white);
    border-radius: 7px;
    display: flex;
    align-items: center;
    justify-content: center;
    font-size: 21px;
    font-weight: 400;
    color: var(--text-white);
    text-decoration: none;
  }
</style>
</head>
<body>
  <section class="banner" aria-label="Clockharbour homepage banner">
    <div class="banner__photo" role="img" aria-label="Photograph of a luxury chronograph wristwatch with a blue dial"></div>

    <p class="banner__question">Prefer to see &amp; try on before purchase?</p>

    <p class="offer">
      <span class="offer__lead">Up to</span>
      <span class="offer__amount">50% OFF!</span>
    </p>

    <svg class="banner__arcs" width="1166" height="110" viewBox="0 0 1166 110" aria-hidden="true">
      <circle cx="960" cy="55" r="79" fill="var(--accent-blue)"/>
      <circle cx="971" cy="55" r="79" fill="var(--banner-black)"/>
      <circle cx="990" cy="55" r="79" fill="var(--accent-blue)"/>
      <circle cx="1005" cy="55" r="79" fill="var(--banner-black)"/>
      <circle cx="1014" cy="55" r="79" fill="var(--accent-blue)"/>
      <rect x="1014" y="0" width="152" height="110" fill="var(--accent-blue)"/>
    </svg>

    <div class="brand">
      <span class="brand__dot"></span>
      <span class="brand__name">clockharbour</span>
    </div>

    <a class="cta" href="#">Visit More</a>
  </section>
</body>
</html>
```